PPT Design Project for an educational startup

We seek a PPT design for a new company based in Japan called "Brivorent".
We provide PPT slide-based educational videos for free.
Please see the link below. You will see some videos.
http://velmora-example.jp/
The current template is also attached.
As we are changing our service name from Velmora to Brivorent, we are considering to change the PPT template as well.
Here are some notes regarding this project.
1. We need three pages;
- Title page: Letters for the tile and the logo are necessary. Some pictorial marks or other design would be appreciated.
- Contents page: Just one line to divide the message part and contents part should be sufficient. Please do not spend your time here.
- Final page: The word "Thank you for watching!" in the center. Some pictorial marks or other design would be appreciated.
2. Please use light green, orange, and purple as main colors. (Same as the current template)
3. You don't have to think about the font-style. This is going to be Japanese font, so we will take care of this.
4. Background color needs to be white, as the slides could be printed out.
5. We use Powerpoint for Mac.
6. No copyright section required, as these slides will be creative commons. Instead of the copyright section, please put the creative commons mark in all slides. (which is in the original template attached)
Updates
Please forget about the creative commons mark.
Hi all,
Target Market(s)
16-25 years old people, who are highly educated or highly motivated for education
Industry/Entity Type
It Company
Requirements
Must have
- 1. Creative commons mark (which is in the original template)
Should not have
- 1. Copyright mark

```html
<!DOCTYPE html>
<html lang="ja">
<head>
<meta charset="UTF-8">
<title>英語学習のゴール</title>
<link rel="stylesheet" href="https://fonts.googleapis.com/css2?family=Noto+Serif+JP:wght@400&family=Noto+Sans+JP:wght@400;700&display=swap">
<style>
  :root {
    --orange: #f79646;
    --orange-deep: #f08a3c;
    --green-light: #c6e0a0;
    --green-band: #9bbb59;
    --grey-strip: #7f7f7f;
    --title-ink: #5a5a5a;
    --brand-ink: #6a6a6a;
    --white: #ffffff;
  }
  html, body {
    margin: 0;
    padding: 0;
    width: 1200px;
    height: 900px;
    overflow: hidden;
    background: var(--white);
  }
  .slide {
    position: relative;
    width: 1200px;
    height: 900px;
    background: var(--white);
    font-family: "Noto Sans JP", sans-serif;
  }
  .header-bar {
    position: absolute;
    left: 0; top: 0;
    width: 1200px; height: 78px;
    background: var(--orange);
    box-shadow: 0 4px 6px rgba(0,0,0,0.25);
    z-index: 2;
  }
  .breadcrumb {
    position: absolute;
    left: 31px; top: 24px;
    margin: 0;
    color: var(--white);
    font-family: "Noto Serif JP", serif;
    font-size: 22px;
    font-weight: 400;
    line-height: 1.2;
    letter-spacing: 0.5px;
  }
  .side-strip {
    position: absolute;
    left: 0; top: 78px;
    width: 25px; height: 822px;
    background: var(--grey-strip);
  }
  .side-panel {
    position: absolute;
    left: 25px; top: 78px;
    width: 283px; height: 807px;
    background: linear-gradient(to bottom, var(--green-light) 0%, #e3f0d0 45%, var(--white) 82%);
  }
  .footer-green {
    position: absolute;
    left: 25px; top: 885px;
    width: 283px; height: 15px;
    background: var(--green-band);
  }
  .footer-orange {
    position: absolute;
    left: 308px; top: 885px;
    width: 892px; height: 15px;
    background: var(--orange);
  }
  .slide-title {
    position: absolute;
    left: 338px; top: 392px;
    margin: 0;
    font-family: "Noto Serif JP", serif;
    font-weight: 400;
    font-size: 56px;
    line-height: 1.2;
    color: var(--title-ink);
    letter-spacing: 1px;
  }
  .brand {
    position: absolute;
    left: 42px; top: 800px;
    margin: 0;
    font-family: "Noto Sans JP", sans-serif;
    font-weight: 700;
    font-size: 48px;
    line-height: 1.2;
    color: var(--brand-ink);
  }
  .corner-squares {
    position: absolute;
    left: 1090px; top: 770px;
  }
</style>
</head>
<body>
  <div class="slide">
    <div class="header-bar">
      <p class="breadcrumb">英語 ＞英語の勉強法</p>
    </div>
    <div class="side-strip"></div>
    <div class="side-panel"></div>
    <div class="footer-green"></div>
    <div class="footer-orange"></div>

    <h1 class="slide-title">英語学習のゴール</h1>

    <p class="brand">Brivorent</p>

    <svg class="corner-squares" width="110" height="110" viewBox="0 0 110 110" aria-hidden="true">
      <rect x="22" y="6" width="28" height="28" fill="var(--orange)"/>
      <rect x="62" y="34" width="32" height="32" fill="var(--orange)"/>
      <rect x="6" y="60" width="43" height="43" fill="var(--orange)"/>
    </svg>
  </div>
</body>
</html>
```